" Produz cachaça artesanal, no interior de Minas Gerais na cidade de Conceição do Mato Dentro Estrada Real, em alambiques de cobre. Produto feito a mao. "

```html
<!DOCTYPE html>
<html lang="pt-BR">
<head>
<meta charset="UTF-8">
<title>Lino Cachaça – Rótulo Cachaça Artesanal</title>
<link rel="stylesheet" href="https://fonts.googleapis.com/css2?family=Italianno&display=swap">
<style>
  :root {
    --backdrop: #ece3d3;
    --parchment-light: #e9dfbf;
    --parchment-dark: #d3c494;
    --ink: #3a2a18;
    --ink-soft: #5a4630;
    --ornament-a: rgba(120, 96, 60, 0.22);
    --ornament-b: rgba(120, 96, 60, 0.05);
  }
  * { box-sizing: border-box; margin: 0; padding: 0; }
  html, body {
    width: 1200px;
    height: 1200px;
    overflow: hidden;
    background: var(--backdrop);
  }
  .canvas {
    position: relative;
    width: 1200px;
    height: 1200px;
    display: flex;
    align-items: center;
    justify-content: center;
  }
  .label {
    position: relative;
    width: 700px;
    height: 940px;
    border-radius: 50% / 37%;
    background: radial-gradient(ellipse at 50% 40%, var(--parchment-light), var(--parchment-dark));
    border: 6px solid var(--ink);
    color: var(--ink);
    font-family: "Italianno", cursive;
    text-align: center;
  }
  .label__inner-frame {
    position: absolute;
    inset: 14px;
    border-radius: 50% / 37%;
    border: 2px solid var(--ink-soft);
  }
  .label__ornament {
    position: absolute;
    left: 130px;
    top: 250px;
    width: 440px;
    height: 480px;
    border-radius: 50%;
    background: radial-gradient(ellipse at center, var(--ornament-a), var(--ornament-b) 70%, transparent);
  }
  .brand {
    position: absolute;
    top: 120px;
    left: 0;
    right: 0;
  }
  .brand__name {
    display: block;
    font-size: 150px;
    line-height: 1;
    font-weight: 400;
  }
  .brand__kind {
    display: block;
    font-size: 50px;
    line-height: 1;
    margin-top: -14px;
    margin-left: 120px;
    color: var(--ink-soft);
  }
  .product {
    position: absolute;
    top: 400px;
    left: 0;
    right: 0;
  }
  .product__title {
    font-size: 104px;
    line-height: 1;
    font-weight: 400;
  }
  .product__origin {
    font-size: 46px;
    line-height: 1;
    margin-top: 10px;
    color: var(--ink-soft);
  }
  .volume {
    position: absolute;
    top: 780px;
    left: 0;
    right: 0;
    padding-left: 200px;
    font-size: 56px;
    line-height: 1;
  }
</style>
</head>
<body>
  <main class="canvas">
    <section class="label">
      <div class="label__inner-frame"></div>
      <div class="label__ornament" role="img" aria-label="Ilustração de dois beija-flores e arabescos em linhas finas"></div>
      <header class="brand">
        <span class="brand__name">Lino</span>
        <span class="brand__kind">Cachaça</span>
      </header>
      <div class="product">
        <h1 class="product__title">Cachaça Artesanal</h1>
        <p class="product__origin">Conceição do Mato Dentro</p>
      </div>
      <p class="volume">750 ml</p>
    </section>
  </main>
</body>
</html>
```